Billboard design 8x3M LUMA (Spanish company)

We´re located in the south of Spain. We run a local telecom company.
We sell Fiber optic, and mobile phone lines mainly.
The billboard will have to be in Spanish, I would like the price to be something you spot on first sight when passing by in the car.
Our company color is blue, like in our logo which I will add. I will also add a example from what we currently have.
The new offer should be:
1000 megas + 100Gigas movil con llamadas ilimitadas. (meaning 1000Mb fiber optic speed and 100Gb data and unlimited calls for 1 mobile line)
Our details are: phone line 956 47 8092
Website: lu-ma.es

```html
<!DOCTYPE html>
<html lang="es">
<head>
<meta charset="UTF-8">
<title>LUMA – Valla 8x3</title>
<link href="https://fonts.googleapis.com/css2?family=Montserrat:wght@600;700;800;900&display=swap" rel="stylesheet">
<style>
  :root {
    --page-bg: #e9edf1;
    --deep-blue: #0c4f7c;
    --mid-blue: #1590d4;
    --sky-blue: #3cbef5;
    --band-blue: #3dbff3;
    --tab-navy: #1c465e;
    --offer-yellow: #ffe500;
    --white: #ffffff;
    --flame-orange: #f47a12;
    --flame-light: #ffb347;
  }
  * { margin: 0; padding: 0; box-sizing: border-box; }
  html, body {
    width: 1200px;
    height: 960px;
    overflow: hidden;
    background: var(--page-bg);
    font-family: "Montserrat", Arial, sans-serif;
  }
  .billboard {
    position: absolute;
    left: 40px;
    top: 260px;
    width: 1120px;
    height: 440px;
    overflow: hidden;
    background: linear-gradient(100deg, var(--deep-blue) 0%, var(--mid-blue) 45%, var(--sky-blue) 75%, var(--sky-blue) 100%);
  }
  .brand {
    position: absolute;
    left: 34px;
    top: 14px;
    color: var(--white);
    font-weight: 900;
    font-size: 80px;
    letter-spacing: 6px;
    line-height: 1;
  }
  .services {
    position: absolute;
    left: 38px;
    top: 100px;
    color: var(--white);
    font-weight: 700;
    font-size: 23px;
    letter-spacing: 0.5px;
  }
  .offer {
    position: absolute;
    left: 30px;
    top: 128px;
    color: var(--offer-yellow);
    font-weight: 900;
    font-size: 96px;
    line-height: 0.9;
    letter-spacing: -1px;
  }
  .offer-detail {
    position: absolute;
    left: 32px;
    top: 306px;
    color: var(--white);
    font-weight: 800;
    font-size: 33px;
    letter-spacing: 1px;
  }
  .contact-band {
    position: absolute;
    left: 0;
    bottom: 0;
    width: 100%;
    height: 86px;
    background: var(--band-blue);
  }
  .phone {
    position: absolute;
    left: 30px;
    top: 12px;
    display: flex;
    align-items: center;
    gap: 10px;
    color: var(--white);
    font-weight: 800;
    font-size: 52px;
    letter-spacing: 1px;
  }
  .phone svg { width: 30px; height: 30px; }
  .web-tab {
    position: absolute;
    left: 470px;
    top: 0;
    width: 310px;
    height: 86px;
    background: var(--tab-navy);
    clip-path: polygon(0 0, 82% 0, 100% 100%, 14% 100%);
    display: flex;
    align-items: center;
    justify-content: center;
    gap: 8px;
    color: var(--white);
    font-weight: 800;
    font-size: 36px;
  }
  .web-tab svg { width: 26px; height: 26px; }
  .hero-art {
    position: absolute;
    left: 760px;
    top: 60px;
    width: 330px;
    height: 340px;
    border-radius: 12px;
    background: radial-gradient(circle at 55% 65%, var(--flame-light) 0%, var(--flame-orange) 45%, rgba(244,122,18,0.0) 80%),
                linear-gradient(160deg, rgba(255,255,255,0.25), rgba(40,20,10,0.35));
  }
</style>
</head>
<body>
  <main class="billboard">
    <div class="brand">LUMA</div>
    <div class="services">Wifi | Fibra | Movil | Tv</div>
    <h1 class="offer">1000 MEGAS<br>+100GIGAS</h1>
    <p class="offer-detail">MOVIL CON LLAMADAS ILIMITADAS.</p>

    <div class="hero-art" role="img" aria-label="Cohete naranja despegando desde la pantalla de un portátil entre una explosión de humo naranja"></div>

    <footer class="contact-band">
      <div class="phone">
        <svg viewBox="0 0 24 24" fill="none" stroke="#ffffff" stroke-width="2" stroke-linecap="round" stroke-linejoin="round" aria-hidden="true">
          <path d="M22 16.9v3a2 2 0 0 1-2.2 2 19.8 19.8 0 0 1-8.6-3.1 19.5 19.5 0 0 1-6-6A19.8 19.8 0 0 1 2.1 4.2 2 2 0 0 1 4.1 2h3a2 2 0 0 1 2 1.7c.1.9.4 1.8.7 2.7a2 2 0 0 1-.5 2.1L8 9.8a16 16 0 0 0 6 6l1.3-1.3a2 2 0 0 1 2.1-.4c.9.3 1.8.6 2.7.7a2 2 0 0 1 1.7 2z"/>
        </svg>
        <span>956 47 8092</span>
      </div>
      <div class="web-tab">
        <svg viewBox="0 0 24 24" fill="none" stroke="#ffffff" stroke-width="1.8" aria-hidden="true">
          <circle cx="12" cy="12" r="10"/>
          <path d="M2 12h20M12 2c3 3 3 17 0 20M12 2c-3 3-3 17 0 20"/>
        </svg>
        <span>lu-ma.es</span>
      </div>
    </footer>
  </main>
</body>
</html>
```